The Quiet Harbor

I have a faux cover I will attach & want you to follow & enhance what I've created. Just an FYI, the book will be posted on brindlo & I'm working with Marrow Lane Publishing.
What you need to know:
The dimensions: 6" x 9" (15.24 x 22.86 cm)
Background color: Black
I did not capture the color of the font, so want you to get a similar gold color.
Font for title, subtitle & author name: Goudy Old Style
Font for "20th Anniversary Edition": Kunstler Script
I have thoughts of shaping the photo in an oval shape -- possibly shade out the edges?

Target Market(s)

All ages: anyone who has encountered issues with doctors, hospitals, and especially those who have struggled with cancer treatment.

Requirements
Nice to have
• Adding below another PDF, showing vintage lines that I would like to see used. Just added some text I will add to the back cover. I am waiting on one more review, which I will add. Attaching that below.

```html
<!DOCTYPE html>
<html lang="en">
<head>
<meta charset="utf-8">
<title>The Quiet Harbor — Cover</title>
<link rel="stylesheet" href="https://fonts.googleapis.com/css2?family=Sorts+Mill+Goudy:ital@0;1&family=Pinyon+Script&display=swap">
<style>
  :root {
    --cover-bg: #242424;
    --gold: #f7c35c;
    --gold-light: #ffe08a;
    --gold-deep: #c8741f;
    --bronze: #8a4a14;
    --photo-light: #e6e6e6;
    --photo-mid: #9a9a9a;
    --photo-dark: #3c3c3c;
  }
  * { margin: 0; padding: 0; box-sizing: border-box; }
  html, body {
    width: 840px;
    height: 1200px;
    overflow: hidden;
    background: var(--cover-bg);
  }
  .cover {
    position: relative;
    width: 840px;
    height: 1200px;
    background: var(--cover-bg);
    color: var(--gold);
    font-family: "Sorts Mill Goudy", "Goudy Old Style", serif;
    text-align: center;
  }
  .cover__title {
    position: absolute;
    top: 120px;
    left: 0;
    width: 100%;
    font-weight: 400;
    font-size: 72px;
    letter-spacing: 1px;
    line-height: 1;
  }
  .cover__subtitle {
    position: absolute;
    top: 240px;
    left: 0;
    width: 100%;
    font-style: italic;
    font-weight: 400;
    font-size: 30px;
    line-height: 46px;
  }
  .cover__edition {
    position: absolute;
    top: 396px;
    left: 0;
    width: 100%;
    font-family: "Pinyon Script", cursive;
    font-size: 31px;
    line-height: 1;
  }
  .cover__edition sup { font-size: 0.55em; }
  .cover__portrait {
    position: absolute;
    left: 52px;
    top: 474px;
    width: 736px;
    height: 556px;
  }
  .cover__author {
    position: absolute;
    top: 1092px;
    left: 0;
    width: 100%;
    font-size: 40px;
    font-weight: 400;
    line-height: 1;
  }
</style>
</head>
<body>
  <main class="cover">
    <h1 class="cover__title">THE QUIET HARBOR</h1>
    <p class="cover__subtitle">A tale of lifelong damage from terminal cancer<br>“treatment” &amp; inhumane doctors</p>
    <p class="cover__edition">20<sup>th</sup> Anniversary Edition</p>

    <svg class="cover__portrait" viewBox="0 0 736 556" aria-hidden="false">
      <defs>
        <linearGradient id="frame-gold" x1="0" y1="0" x2="1" y2="1">
          <stop offset="0" stop-color="var(--gold-light)"/>
          <stop offset="0.45" stop-color="var(--gold)"/>
          <stop offset="0.8" stop-color="var(--gold-deep)"/>
          <stop offset="1" stop-color="var(--bronze)"/>
        </linearGradient>
        <radialGradient id="photo-tone" cx="0.5" cy="0.45" r="0.6">
          <stop offset="0" stop-color="var(--photo-light)"/>
          <stop offset="0.6" stop-color="var(--photo-mid)"/>
          <stop offset="1" stop-color="var(--photo-dark)"/>
        </radialGradient>
      </defs>
      <ellipse class="frame-ring" cx="368" cy="278" rx="364" ry="274"
               fill="url(#frame-gold)" role="img"
               aria-label="Ornate gold and bronze filigree oval frame"/>
      <ellipse class="frame-inner-edge" cx="368" cy="278" rx="334" ry="244"
               fill="none" stroke="var(--bronze)" stroke-width="3"/>
      <ellipse class="portrait-photo" cx="368" cy="278" rx="330" ry="240"
               fill="url(#photo-tone)" role="img"
               aria-label="Black and white portrait photograph of the author smiling, seated in a living room"/>
    </svg>

    <p class="cover__author">Helen Marsh</p>
  </main>
</body>
</html>
```